Bold, Modern, Clean "Vernatouchmassage.com" website

Why we stand out?
We are a male and female mobile massage team. Our names are Jonah and Tessa. 
Verna Touch is a Seattle based mobile massage service. Our massage is offered to the community with a goal of facilitating balance within each individual. We specialize in integrated Pain management, and sports/medical massage therapy. Every client's first assessment is attended by our male and female massage therapist team. Depending on the goals identified for an individual determines which therapist will be assigned to provide treatment, if not both.

Our passion...
Here at Verna Touch, we have a great passion for Postural Resoration and how it is integrated into an individual's Massage treatment. We pride ourselves in being natural facilitators of healing, which takes the ego of the therapist out of the client's healing process. We strive to deliver the best massage possible by including modalities such as Neuromuscular, Myofascial release, spontaneous muscle release, postural restoration, orthopedic, and medical massage.

Our education...

We are both Graduates of Alvenra, school of massage therapy. We have continuing education in medical massage, myofacial release, trigger point therapy, postural restoration, anatomy, and spontaneous muscle release. Tessa is also a Certified Yoga Instructor, which amplifies her experience with flexibility and strength as it pertains to each individual. Jonah's passion is Massage, stretching, and strength training to encourage postural restoration and realignment.

Our rates-

Our rates are $75/ 60 minutes, $95/ 90 minutes, and $120/ 120 minutes.

Education-
Both Tessa and I worked as behavioral health professionals that specialized in life skills mentoring for youth who had experienced different types of trauma. This led us both to want to help others in a different environment, where individuals can be empowered to take responsibility over their own healing. To us, massage is a type of manipulation physical therapy, that encourages healing on many levels.

Advice to any massage client-
The most important thing to 'us', as Licenced providers is to get you on to our table to show you our skills. But a good therapist never forgets that it's not about what we do for you, but what we can facilitate for you. Your health and healing has nothing to do with us. It is yours, not ours. Identify what your goals are with any Therapist, and know what the end looks like. Progress should be tangible, such as range of motion, and decreased pain.

5/5 stars Massage Therapy
Verified Review

Tessa and Jonah at Verna Touch are awesome! I recently had open heart surgery, and Tessa worked on me to increase my range of motion while helping with the pinched nerve from my arm being in the same position for so long during my surgery. My wife drives a lot for work, and Jonah has helped decrease her neck and lower back pain immensely. They are seriously the best therapists I have ever worked with. I would recommend them to anyone who needs anything from stress relief to a medical massage treatment. They are professional, up beat, easy going, and always on time. And, I love that they meet us where ever we like! We did a staycation recently, where they came to our hotel to give us relaxation massages. Although usually they come to our home, where we focus on pain related issues. We will continue to work with them for a long, long time.

Brisa K. on December 17, 2015

Target Market(s)

Mobile massage therapy clients

Industry/Entity Type

Massage Therapy

Coding

Coded - Design and coding required

Number of Pages Required

1 page

Font styles to use
Serif
Sans Serif

Requirements
Must have
• Please add or remove any information that would help the presentation of our website. Our logo is posted below, please include into the website.
• Please include a contact field that includes, vernatouchmassage@quillmail.test,
• (206) 555-0147
• We have also included our own stock photos, as well as a photo of Jonah and Tessa. Please include a cropped photo of both massage therapists.

```html
<!DOCTYPE html>
<html lang="en">
<head>
<meta charset="utf-8">
<title>Verna Touch – Mobile Massage</title>
<link href="https://fonts.googleapis.com/css2?family=Lato:ital,wght@0,400;0,700;1,400&display=swap" rel="stylesheet">
<style>
:root{
  --teal:#1fc9c4;
  --teal-dark:#0fb3b2;
  --blue:#1b2fb8;
  --blue-band:#2a3fc4;
  --ink:#2b2b2b;
  --body:#444;
  --grey-band:#5a5a5a;
  --footer:#1c1c1c;
  --white:#fff;
}
*{box-sizing:border-box;margin:0;padding:0}
html,body{width:1200px;height:2903px;overflow:hidden}
body{font-family:'Lato',sans-serif;color:var(--body);background:var(--white);position:relative}
.abs{position:absolute}
.topbar{top:0;left:0;width:1200px;height:78px;background:#fff}
.contact{top:24px;display:flex;align-items:center;gap:14px;font-size:19px;color:var(--blue)}
.contact.phone{left:84px;font-weight:700}
.contact.mail{right:88px;font-size:16px}
.nav{top:78px;left:0;width:1200px;height:44px;background:linear-gradient(#5fe0dc,var(--teal-dark));display:flex;align-items:center}
.nav a{position:absolute;color:#fff;font-weight:700;font-size:16px;text-decoration:none}
.brand{top:14px;left:513px;width:174px;height:174px;border-radius:50%;background:var(--blue);border:6px solid #fff;box-shadow:0 2px 8px rgba(0,0,0,.25);display:flex;align-items:center;justify-content:center;z-index:3}
.brand span{color:#fff;font-weight:700;font-size:30px;text-align:center;line-height:1.05}
.hero{top:122px;left:0;width:1200px;height:581px;background:linear-gradient(90deg,#d9ddd6 0%,#ebeeea 45%,#e7ddd3 70%,#cfc5bb 100%)}
.hero h1{position:absolute;left:91px;top:172px;width:520px;font-size:33px;line-height:49px;font-weight:700;color:#2e2e2e}
.hero .arrow{position:absolute;top:265px}
.dots{display:flex;gap:6px}
.dots i{width:10px;height:10px;border-radius:50%;background:#b9dcd4;display:block}
.dots i.on{background:var(--blue)}
.section-title{position:absolute;left:0;width:1200px;text-align:center;font-size:33px;font-weight:400}
.divider{position:absolute;left:325px;width:550px;height:16px}
.para{position:absolute;left:110px;width:980px;text-align:center;font-size:14.5px;line-height:25px}
.band-dark{left:0;width:1200px;background:linear-gradient(90deg,#4d4d4d,#6a6663 50%,#4e4c4a)}
.band-dark .section-title,.band-dark .para{color:#fff}
.card{top:1360px;width:320px;height:396px;background:#fff;border-top:3px solid var(--teal);border-bottom:3px solid var(--blue);box-shadow:0 0 4px rgba(0,0,0,.2)}
.card h2{position:absolute;left:18px;top:12px;font-size:29px;font-weight:700;color:var(--teal-dark)}
.card h2 b{color:var(--blue)}
.card .media{position:absolute;left:18px;top:64px;width:284px;height:124px;border:1px solid #ccc}
.card p{position:absolute;left:18px;top:198px;width:284px;font-size:13.5px;line-height:19.5px;color:#333}
.rates{list-style:none;position:absolute;left:18px;top:290px;font-size:19px;color:#333}
.rates li{display:flex;align-items:center;gap:10px;height:31px}
.review{position:absolute;left:150px;top:2289px;width:900px;text-align:center;font-style:italic;font-size:13.5px;line-height:25px;color:#555}
.stars{position:absolute;left:0;width:1200px;text-align:center;font-style:italic;font-size:14px;color:var(--blue);top:2458px}
.inquiry{top:2573px;left:0;width:1200px;height:223px;background:var(--blue-band)}
.inquiry .section-title{color:#fff;top:30px}
.field{position:absolute;top:140px;height:46px;background:#fff;border:none;font-family:inherit;font-size:14px;padding-left:14px;color:#777;display:flex;align-items:center}
.submit{position:absolute;top:140px;left:913px;width:202px;height:46px;background:#1a1a1a;color:#fff;font-weight:700;font-size:20px;display:flex;align-items:center;justify-content:center}
.footer{top:2796px;left:0;width:1200px;height:107px;background:var(--footer);color:#fff;text-align:center}
.footer nav{position:absolute;top:28px;width:1200px;font-size:14px}
.footer nav span{margin:0 8px}
.footer nav em{font-style:normal;color:#888}
.footer small{position:absolute;top:66px;left:0;width:1200px;font-size:13.5px;color:#ddd}
</style>
</head>
<body>
<header class="abs topbar">
  <div class="abs contact phone">
    <svg width="30" height="30" viewBox="0 0 30 30"><circle cx="15" cy="15" r="13" fill="none" stroke="#1b2fb8" stroke-width="2"/><path d="M10 8c1-1 2 0 3 2s0 2-1 3c1 2 3 4 5 5 1-1 1-2 3-1s3 2 2 3c-1 2-3 3-6 1-3-2-6-5-7-8-1-2 0-4 1-5z" fill="#1b2fb8"/></svg>
    (206) 555-0147
  </div>
  <div class="abs contact mail">
    <svg width="30" height="30" viewBox="0 0 30 30"><circle cx="15" cy="15" r="13" fill="none" stroke="#1b2fb8" stroke-width="2"/><rect x="8" y="10" width="14" height="10" fill="#1b2fb8"/><path d="M8 10l7 6 7-6" stroke="#fff" fill="none" stroke-width="1.5"/></svg>
    vernatouchmassage@quillmail.test
  </div>
</header>
<nav class="abs nav">
  <a style="left:87px">Why We Stand Out?</a>
  <a style="left:282px">Our Passion</a>
  <a style="left:416px">Education</a>
  <a style="left:712px">Rates</a>
  <a style="left:786px">Advice To Any Massage Client</a>
  <a style="left:1048px">Reviews</a>
</nav>
<div class="abs brand"><span>Verna<br>Touch</span></div>

<section class="abs hero" role="img" aria-label="Therapist guiding a woman through a resistance band stretch in a bright room">
  <h1>We Are A Seattle Based Mobile Massage Service Specialize In Integrated Pain Management, And Sports/medical Massage Therapy.</h1>
  <svg class="arrow" style="left:40px" width="24" height="46"><path d="M20 3L4 23l16 20" stroke="#fff" stroke-width="2" fill="none"/></svg>
  <svg class="arrow" style="right:40px" width="24" height="46"><path d="M4 3l16 20L4 43" stroke="#fff" stroke-width="2" fill="none"/></svg>
  <div class="dots" style="position:absolute;left:296px;top:440px"><i class="on"></i><i></i><i></i></div>
</section>

<section>
  <h2 class="section-title" style="top:742px;color:var(--ink)">Why We Stand Out?</h2>
  <svg class="divider" style="top:801px"><line x1="0" y1="8" x2="245" y2="8" stroke="#1fc9c4"/><line x1="305" y1="8" x2="550" y2="8" stroke="#1fc9c4"/><circle cx="255" cy="8" r="5" fill="none" stroke="#1fc9c4" stroke-width="1.5"/><circle cx="275" cy="8" r="6.5" fill="none" stroke="#1fc9c4" stroke-width="1.5"/><circle cx="275" cy="8" r="3.5" fill="#1b2fb8"/><circle cx="295" cy="8" r="5" fill="none" stroke="#1fc9c4" stroke-width="1.5"/></svg>
  <p class="para" style="top:838px;color:#333">We are a male and female mobile massage team. Our names are Jonah and Tessa. Verna Touch is a Seattle based mobile massage service. Our massage is offered to the community with a goal of facilitating balance within each individual. We specialize in integrated Pain management, and sports/medical massage therapy. Every client's first assessment is attended by our male and female massage therapist team. Depending on the goals identified for an individual determines which therapist will be assigned to provide treatment, if not both.</p>
</section>

<section class="abs band-dark" style="top:987px;height:315px" role="img" aria-label="Client resting face down during a massage, dimmed backdrop">
  <h2 class="section-title" style="top:52px">Our Passion</h2>
  <svg class="divider" style="top:107px"><line x1="0" y1="8" x2="245" y2="8" stroke="#ddd"/><line x1="305" y1="8" x2="550" y2="8" stroke="#ddd"/><circle cx="255" cy="8" r="5" fill="none" stroke="#fff" stroke-width="1.5"/><circle cx="275" cy="8" r="6.5" fill="none" stroke="#fff" stroke-width="1.5"/><circle cx="275" cy="8" r="3.5" fill="#fff"/><circle cx="295" cy="8" r="5" fill="none" stroke="#fff" stroke-width="1.5"/></svg>
  <p class="para" style="top:160px;font-weight:700;width:1010px;left:95px">We are both Graduates of Alvenra, school of massage therapy. We have continuing education in medical massage, myofacial release, trigger point therapy, postural restoration, anatomy, and spontaneous muscle release. Tessa is also a Certified Yoga Instructor, which amplifies her experience with flexibility and strength as it pertains to each individual. Jonah's passion is Massage, stretching, and strength training to encourage postural restoration and realignment.</p>
</section>

<article class="abs card" style="left:83px">
  <h2>About <b>Jonah</b></h2>
  <div class="media" role="img" aria-label="Cropped photo of Jonah, massage therapist" style="background:linear-gradient(90deg,#e8ecef,#f5f3f0 55%,#d9c7b5)"></div>
  <p style="text-align:justify;letter-spacing:.3px">Jonah Graduate of Alvenra, school of massage therapy, ontinuing education in medical massage, myofacial release, trigger point therapy, postural restoration, anatomy, and spontaneous muscle releaseJonah's passion is Massage, stretching, and strength training to encourage postural restoration and realignment.</p>
</article>
<article class="abs card" style="left:441px">
  <h2>About <b>Tessa</b></h2>
  <div class="media" role="img" aria-label="Cropped photo of Tessa, massage therapist and yoga instructor" style="background:linear-gradient(90deg,#eceae6,#f0e2d2 50%,#e6e4e0)"></div>
  <p>Tessa is also a Certified Yoga Instructor, which amplifies her experience with flexibility and strength as it pertains to each individual. I worked as behavioral health professionals that specialized in life skills mentoring for youth who had experienced different types of trauma and massage is a type of manipulation physical therapy, that encourages healing on many levels.</p>
</article>
<article class="abs card" style="left:795px">
  <h2>Our <b>Rates</b></h2>
  <div class="media" role="img" aria-label="Spa still life with stacked black stones and a purple orchid" style="background:linear-gradient(90deg,#f4f4f4 0%,#e9eef0 45%,#8c7a9e 75%,#2c2c2c 100%)"></div>
  <p style="top:202px">Lorem ipsum dolor sit amet, consectetuer adipiscing elit, sed diam nonummy nibh euismod tincidunt ut laoreet dolore magna aliquam erat volutpat.</p>
  <ul class="rates">
    <li><svg width="18" height="16"><path d="M2 8l5 5L16 2" stroke="#0fb3b2" stroke-width="3" fill="none"/></svg>$75/ 60 minutes</li>
    <li><svg width="18" height="16"><path d="M2 8l5 5L16 2" stroke="#0fb3b2" stroke-width="3" fill="none"/></svg>$95/ 90 minutes</li>
    <li><svg width="18" height="16"><path d="M2 8l5 5L16 2" stroke="#0fb3b2" stroke-width="3" fill="none"/></svg>$120/ 120 minutes</li>
  </ul>
</article>

<section class="abs band-dark" style="top:1809px;height:318px" role="img" aria-label="Massage session with hands on a client's back, dimmed backdrop">
  <h2 class="section-title" style="top:62px">Advice To Any Massage Client</h2>
  <svg class="divider" style="top:117px"><line x1="0" y1="8" x2="245" y2="8" stroke="#ddd"/><line x1="305" y1="8" x2="550" y2="8" stroke="#ddd"/><circle cx="255" cy="8" r="5" fill="none" stroke="#fff" stroke-width="1.5"/><circle cx="275" cy="8" r="6.5" fill="none" stroke="#fff" stroke-width="1.5"/><circle cx="275" cy="8" r="3.5" fill="#fff"/><circle cx="295" cy="8" r="5" fill="none" stroke="#fff" stroke-width="1.5"/></svg>
  <p class="para" style="top:164px;font-size:16px;line-height:26px;left:95px;width:1010px">The most important thing to 'us', as Licenced providers is to get you on to our table to show you our skills. But a good therapist never forgets that it's not about what we do for you, but what we can facilitate for you. Your health and healing has nothing to do with us. It is yours, not ours. Identify what your goals are with any Therapist, and know what the end looks like. Progress should be tangible, such as range of motion, and decreased pain.</p>
</section>

<section>
  <h2 class="section-title" style="top:2181px;color:var(--ink)">Client Reviews</h2>
  <svg class="divider" style="top:2240px"><line x1="0" y1="8" x2="245" y2="8" stroke="#1fc9c4"/><line x1="305" y1="8" x2="550" y2="8" stroke="#1fc9c4"/><circle cx="255" cy="8" r="5" fill="none" stroke="#1fc9c4" stroke-width="1.5"/><circle cx="275" cy="8" r="6.5" fill="none" stroke="#1fc9c4" stroke-width="1.5"/><circle cx="275" cy="8" r="3.5" fill="#1b2fb8"/><circle cx="295" cy="8" r="5" fill="none" stroke="#1fc9c4" stroke-width="1.5"/></svg>
  <svg class="abs" style="left:40px;top:2318px" width="16" height="30"><path d="M13 3L3 15l10 12" stroke="#bbb" stroke-width="2" fill="none"/></svg>
  <svg class="abs" style="right:40px;top:2318px" width="16" height="30"><path d="M3 3l10 12L3 27" stroke="#bbb" stroke-width="2" fill="none"/></svg>
  <div class="abs" style="left:84px;top:2278px;font-size:46px;color:#ccc;font-family:Georgia,serif">“</div>
  <div class="abs" style="left:1090px;top:2390px;font-size:46px;color:#ccc;font-family:Georgia,serif">”</div>
  <p class="review">Tessa and Jonah at Verna Touch are awesome! I recently had open heart surgery, and Tessa worked on me to increase my range of motion while helping with the pinched nerve from my arm being in the same position for so long during my surgery. My wife drives a lot for work, and Jonah has helped decrease her neck and lower back pain immensely. They are seriously the best therapists I have ever worked with. I would recommend them to anyone who needs anything from stress relief to a medical massage treatment. They are professional, upbeat, easy going, and always on time. And, I love that they meet us where ever we like! We did a staycation recently, where they came to our hotel to give us relaxation massages. Although usually they come to our home, where we focus on pain related issues. We will continue to work with them for a long, long time.</p>
  <p class="stars">5/5 stars Massage TherapyVerified Review</p>
  <svg class="abs" style="left:555px;top:2494px" width="90" height="30"><rect x="0" y="0" width="90" height="30" rx="3" fill="#e9e4d6"/></svg>
</section>

<section class="abs inquiry">
  <h2 class="section-title">Quick Inquiry</h2>
  <svg class="divider" style="top:89px"><circle cx="255" cy="8" r="5" fill="none" stroke="#fff" stroke-width="1.5"/><circle cx="275" cy="8" r="6.5" fill="none" stroke="#fff" stroke-width="1.5"/><circle cx="275" cy="8" r="3.5" fill="#fff"/><circle cx="295" cy="8" r="5" fill="none" stroke="#fff" stroke-width="1.5"/></svg>
  <div class="field" style="left:83px;width:207px">Name</div>
  <div class="field" style="left:312px;width:207px">Email</div>
  <div class="field" style="left:538px;width:358px">Message</div>
  <div class="submit">Submit</div>
</section>

<footer class="abs footer">
  <nav><span>Why We Stand Out?</span><em>•</em><span>Our Passion</span><em>•</em><span>Education</span><em>•</em><span>Rates</span><em>•</em><span>Advice To Any Massage Client</span><em>•</em><span>Reviews</span></nav>
  <small>© 2015 Verna Touch Mobile Massage. All Rights Reserved.</small>
</footer>
</body>
</html>
```